Flyer-Design für Österreichische Bienen-Aktie
Super so wie ich es mir vorgestellt habe!!!
Zielgruppe
Firma FlorWerk
Zielgruppe ist jeder der sich mit Umweltschutz / Nachhaltigkeit / BIO ausseinandersetzt.
Aufgabenstellung
Das Format ist DinLang
Datenformat (inkl. 2,00 mm Beschnitt): 21,40 x 21,40 cm
Endformat (offen): 21,00 x 21,00 cm
Endformat (geschlossen): 10,50 x 21,00 cm
Was soll am Flyer stehen.
Die Stilrichtung in Richtung ÖKO bitte
Erste Österreichische Bienen-Aktie
Noch nie schmeckte Ihnen Ihr Investment so gut.
Kosten pro Aktie 250,-- exkl. MwSt.
was bekommt man 5 Jahre lang 3,5 Kg Honig ergibt mit dem Heutigem Honigpreis von 14,90 je kg am Ende der Laufzeit 260,75€
Mit Ihrem Engagement sichern Sie Tausenden dieser wundervollen Nützlinge das Überleben und ermöglichen eine intensive und nachhaltige Betreuung durch FlorWerk.
Was wird mit dem Geld gemacht?
Zum einen werden Bienenvölker zugekauft zum anderen wird in sogenannte Bienenoasen Investiert.
Bienenoasen sind Rückzugsgebiete in denen sich alle Insekten erholen können. Wie sehen solche Oasen aus? Ein kleiner Vorgeschmack unter https://www.videoportal-beispiel.de/watch?v=qR_8TL-ZP2N
Auf diesen Bienenoasen werden Blumen Bäume und Sträucher gesetzt die als Nahrungsgrundlage für alle bestäubenden Insekten dienen.
Ihre Dividende (Honig)
Die Honiggläser werden individuell gebrandet Sprich sie können den Honig weiterschenken oder auch gerne Selber Essen. Es ist vieles Möglich Logo / Texte / Fotos können am Honigglas angebracht werden. Für Firmen gegen Aufpreis ist das abfüllen in vielen Kleingläser möglich = Ideale Werbung!

```html
<!DOCTYPE html>
<html lang="de">
<head>
<meta charset="utf-8">
<title>Erste Österreichische Bienen-Aktie – Flyer</title>
<link rel="stylesheet" href="https://fonts.googleapis.com/css2?family=Cinzel:wght@400;700&family=Great+Vibes&display=swap">
<style>
  :root {
    --canvas: #ffffff;
    --paper: #f4f2ec;
    --honey-red: #c4524c;
    --text-red: #b44a44;
    --ink: #3a3330;
    --rule: #5a514d;
    --flower-teal: #5fa7a8;
    --flower-orange: #f0a070;
    --flower-red: #e07060;
    --white: #ffffff;
  }
  * { box-sizing: border-box; margin: 0; padding: 0; }
  html, body { width: 1200px; height: 674px; overflow: hidden; background: var(--canvas); }
  body { position: relative; font-family: "Cinzel", serif; color: var(--text-red); }

  .panel {
    position: absolute;
    top: 133px;
    width: 533px;
    height: 532px;
    background: var(--paper);
    overflow: hidden;
  }
  .panel--cover { left: 2px; }
  .panel--inside { left: 548px; }

  /* cover */
  .bee-illustration {
    position: absolute;
    background: radial-gradient(ellipse at center, #5a504c 0%, #8a817c 45%, rgba(244,242,236,0) 72%);
  }
  .panel--cover .bee-illustration { left: 339px; top: 53px; width: 92px; height: 66px; }

  .sender {
    position: absolute;
    left: 70px; top: 187px; width: 160px;
    text-align: center;
    font-size: 7.5px;
    line-height: 15.5px;
    color: var(--text-red);
  }

  .cover-title {
    position: absolute;
    left: 292px; top: 142px; width: 198px;
    text-align: center;
  }
  .cover-title .kicker { font-size: 15.5px; letter-spacing: 0.3px; line-height: 20px; }
  .cover-title .rule { height: 1px; background: var(--rule); margin: 3px 0; }
  .cover-title .word {
    font-size: 57px; line-height: 50px; letter-spacing: 1px; font-weight: 400;
  }
  .cover-title .word:first-of-type { margin-top: 6px; }
  .cover-title .rule--bottom { margin-top: 8px; }

  .flower-meadow {
    position: absolute; left: 0; bottom: 0; width: 100%;
    background: linear-gradient(180deg, rgba(244,242,236,0) 0%, rgba(224,112,96,0.35) 30%, rgba(95,167,168,0.4) 65%, rgba(240,160,112,0.35) 100%);
  }
  .panel--cover .flower-meadow { height: 253px; }
  .panel--inside .flower-meadow { height: 174px; opacity: 0.45; }

  .ribbon {
    position: absolute;
    width: 222px; height: 46px;
    transform: rotate(-10deg);
  }
  .ribbon svg { position: absolute; inset: 0; width: 100%; height: 100%; }
  .ribbon .slogan {
    position: relative;
    font-family: "Great Vibes", cursive;
    color: var(--white);
    font-size: 14.5px;
    line-height: 15px;
    text-align: center;
    padding-top: 8px;
  }
  .panel--cover .ribbon { left: 281px; top: 420px; }
  .panel--inside .ribbon { left: 286px; top: 419px; }

  /* inside */
  .title-band {
    position: absolute; left: 0; top: 97px; width: 100%; height: 72px;
    background: var(--honey-red);
    color: var(--white);
  }
  .title-band .kicker { position: absolute; left: 28px; top: 12px; font-size: 16px; letter-spacing: 0.5px; }
  .title-band .name { position: absolute; left: 28px; top: 32px; font-size: 34px; letter-spacing: 0.5px; }
  .panel--inside .bee-illustration { left: 374px; top: 105px; width: 136px; height: 88px;
    background: radial-gradient(ellipse at center, #6e2a26 0%, #9a3c37 45%, rgba(196,82,76,0) 72%); }

  .column {
    position: absolute; top: 216px; width: 230px;
    font-size: 6.6px; line-height: 11.4px; color: var(--text-red);
  }
  .column--left { left: 25px; }
  .column--right { left: 282px; }
  .column p { margin-bottom: 11.4px; }
  .column .facts { display: grid; grid-template-columns: 86px 1fr; }
  .column .facts dt { font-weight: 700; }
  .column h2 { font-size: 9.5px; line-height: 13px; font-weight: 700; margin-top: 2px; }
  .column .url { word-break: break-all; }
</style>
</head>
<body>

<section class="panel panel--cover">
  <div class="bee-illustration" role="img" aria-label="Gestochene Illustration einer Honigbiene"></div>

  <address class="sender" style="font-style:normal">
    FlorWerk<br>
    Blütenland GmbH<br>
    Lindenweg 14<br>
    7100 Musterdorf am See<br>
    office@florwerk.at
  </address>

  <header class="cover-title">
    <div class="kicker">Erste Österreichische</div>
    <div class="rule"></div>
    <div class="word">Bienen</div>
    <div class="word">Aktie</div>
    <div class="rule rule--bottom"></div>
  </header>

  <div class="flower-meadow" role="img" aria-label="Linienzeichnung einer Wildblumenwiese mit Mohn, Kornblumen und Lilien in Rot, Orange und Türkis"></div>

  <div class="ribbon">
    <svg viewBox="0 0 222 46" preserveAspectRatio="none" aria-hidden="true">
      <polygon points="0,4 222,4 208,23 222,42 0,42 14,23" fill="var(--honey-red)"/>
    </svg>
    <p class="slogan">Noch nie schmeckte Ihnen<br>Ihr Investment so gut.</p>
  </div>
</section>

<section class="panel panel--inside">
  <div class="title-band">
    <div class="kicker">Erste Österreichische</div>
    <h1 class="name" style="font-weight:400">BienenAktie</h1>
  </div>
  <div class="bee-illustration" role="img" aria-label="Gestochene Illustration einer fliegenden Honigbiene"></div>

  <div class="column column--left">
    <dl class="facts">
      <dt>Kosten pro Aktie:</dt><dd>250,-- exkl. MwSt.</dd>
      <dt>was bekommt man:</dt><dd>5 Jahre lang 3,5 Kg Honig</dd>
    </dl>
    <p style="margin-top:11.4px">ergibt mit dem Heutigem Honigpreis von 14,90 je kg am Ende der Laufzeit 260,75€<br>
    Mit Ihrem Engagement sichern Sie Tausenden dieser wundervollen Nützlinge das Überleben und ermöglichen eine intensive und nachhaltige Betreuung durch FlorWerk.</p>
    <h2>Was wird mit dem Geld gemacht?</h2>
    <p>Zum einen werden Bienenvölker zugekauft zum anderen wird in sogenannte Bienenoasen investiert. Bienenoasen sind Rückzugsgebiete in denen sich alle</p>
  </div>

  <div class="column column--right">
    <p>Insekten erholen können. Wie sehen solche Oasen aus? Ein kleiner Vorgeschmack unter <span class="url">https://www.videoportal-beispiel.de/watch?v=qR_8TL-ZP2N</span><br>
    Auf diesen Bienenoasen werden Blumen Bäume und Sträucher gesetzt die als Nahrungsgrundlage für alle bestäubenden Insekten dienen.</p>
    <h2>Ihre Dividende (Honig)</h2>
    <p>Die Honiggläser werden individuell gebrandet sprich sie können den Honig weiterschenken oder auch gerne selber essen. Es ist vieles möglich Logo / Texte / Fotos können am Honigglas angebracht werden. Für Firmen gegen Aufpreis ist das abfüllen in vielen Kleingläser möglich = Ideale Werbung!</p>
  </div>

  <div class="flower-meadow" role="img" aria-label="Blasse Linienzeichnung einer Wildblumenwiese"></div>

  <div class="ribbon">
    <svg viewBox="0 0 222 46" preserveAspectRatio="none" aria-hidden="true">
      <polygon points="0,4 222,4 208,23 222,42 0,42 14,23" fill="var(--honey-red)"/>
    </svg>
    <p class="slogan">Noch nie schmeckte Ihnen<br>Ihr Investment so gut.</p>
  </div>
</section>

</body>
</html>
```